Logo Design with Business Card Project

Attractive Logo with colourful background !
I have uploaded a new image of the updated Home page with the Real Estate landing page for your reference.
We are looking for a Business card design which easily identifies us as a Video classifieds company.

Target Market(s)

20 - 35 yr old people who are connected through social media

Industry/Entity Type

Business

Logo Text

KEB DOZ AM

Logo styles of interest
Abstract Logo
Requirements
Must have
• Simple layout with striking / engaging colours
Nice to have
• Require an updated logo to go on business card / home page

```html
<!DOCTYPE html>
<html lang="en">
<head>
<meta charset="utf-8">
<title>KEB DOZ AM – Business Card</title>
<link href="https://fonts.googleapis.com/css2?family=Gelasio:wght@700&display=swap" rel="stylesheet">
<style>
  :root {
    --page-bg: #e9ebef;
    --blue-deep: #1e2a7a;
    --blue-mid: #2a5bb8;
    --blue-bright: #27a3e0;
    --blue-panel-dark: #24358f;
    --blue-panel-light: #2f7ccc;
    --text-white: #ffffff;
    --text-yellow: #ffe81a;
    --text-shadow: rgba(10, 14, 60, 0.75);
    --card-w: 840px;
    --card-h: 480px;
  }
  * { box-sizing: border-box; margin: 0; padding: 0; }
  html, body {
    width: 1200px; height: 1200px; overflow: hidden;
    background: var(--page-bg);
    font-family: "Gelasio", Georgia, serif;
    font-weight: 700;
  }
  .sheet {
    width: 1200px; height: 1200px;
    display: flex; flex-direction: column; align-items: center; justify-content: center;
    gap: 60px;
  }
  .card {
    position: relative;
    width: var(--card-w); height: var(--card-h);
    overflow: hidden;
    box-shadow: 0 6px 18px rgba(0, 0, 0, 0.25);
  }
  .card-pattern {
    position: absolute; left: 0; top: 0; width: 100%;
    background:
      linear-gradient(135deg, rgba(255,255,255,0.06) 0%, rgba(0,0,0,0.08) 50%, rgba(255,255,255,0.06) 100%),
      linear-gradient(90deg, var(--blue-deep) 0%, var(--blue-bright) 30%, var(--blue-mid) 55%, var(--blue-bright) 80%, var(--blue-deep) 100%);
  }
  .card-front .card-pattern { height: 100%; }
  .card-back .card-pattern { height: 38%; }
  .card-back .card-panel {
    position: absolute; left: 0; bottom: 0; width: 100%; height: 62%;
    background: linear-gradient(100deg, var(--blue-panel-dark) 0%, var(--blue-panel-light) 70%, var(--blue-panel-dark) 100%);
  }
  .wordmark {
    position: absolute;
    color: var(--text-white);
    white-space: nowrap;
    letter-spacing: 2px;
  }
  .card-front .wordmark {
    top: 95px; left: 0; width: 100%; text-align: center;
    font-size: 84px;
  }
  .card-back .wordmark {
    top: 62px; left: 50px;
    font-size: 40px;
  }
  .tagline {
    position: absolute; left: 0; width: 100%; top: 320px;
    text-align: center; font-size: 36px; line-height: 1.25;
    text-shadow: 2px 2px 2px var(--text-shadow);
  }
  .tagline .line-white { color: var(--text-white); display: block; }
  .tagline .line-yellow { color: var(--text-yellow); display: block; }
  .identity {
    position: absolute; right: 36px; top: 48px; text-align: right;
    text-shadow: 2px 2px 2px var(--text-shadow);
  }
  .identity .person-name { color: var(--text-white); font-size: 34px; display: block; }
  .identity .person-role { color: var(--text-yellow); font-size: 34px; display: block; margin-top: 2px; }
  .contact {
    position: absolute; left: 230px; top: 262px;
    list-style: none; font-size: 34px; line-height: 1.18;
    text-shadow: 2px 2px 2px var(--text-shadow);
  }
  .contact .label { color: var(--text-yellow); display: inline-block; min-width: 74px; }
  .contact .value { color: var(--text-white); }
  .contact .web { color: var(--text-yellow); }
</style>
</head>
<body>
  <main class="sheet">
    <section class="card card-front" aria-label="Business card front">
      <div class="card-pattern" role="img" aria-label="Blue faceted triangle pattern background"></div>
      <div class="wordmark">KEB DOZ AM</div>
      <p class="tagline">
        <span class="line-white">Buy and sell through the</span>
        <span class="line-yellow">No.1 Video Classifieds</span>
      </p>
    </section>

    <section class="card card-back" aria-label="Business card back">
      <div class="card-pattern" role="img" aria-label="Blue faceted triangle pattern band"></div>
      <div class="card-panel"></div>
      <div class="wordmark">KEB DOZ AM</div>
      <div class="identity">
        <span class="person-name">Daniel Vorstrand</span>
        <span class="person-role">Managing Director</span>
      </div>
      <ul class="contact">
        <li><span class="label">E:</span><span class="value">daniel@kebdozam.com</span></li>
        <li><span class="web">www.kebdozam.com</span></li>
        <li><span class="label">Ph:</span><span class="value">+617 5550 1846</span></li>
        <li><span class="label">M:</span><span class="value">0400 555 182</span></li>
      </ul>
    </section>
  </main>
</body>
</html>
```